Post Card Mailer for QUIK PATH PROSPECTS using new logo

We need a post card designed to send through the USA mail service that will go to new prospective clients.

The post card will introduce me and my new company and try to educate them our on company and services.

The goal is for them to call me or email me so I can have a discussion and try to sell our product.

Our product is a name list of individuals that are looking for consulting / help to determine if they qualify for USA social security benefits and then help to manage the process. We sell this name list to law firms that help these individuals.

Our services are better because we have a better less expensive way to identify people via the internet that want help. Our conversion rate is 15%, so every 100 leads a law firm buys the will obtain 15 customers / clients.

Designer on Logo took alot longer than expected. Also there were two projects that needed to combined into one. Which was done yesterday.

Target Market(s)

Law firms

Font styles to use
Serif
Sans Serif
Script

Colors

Designer to choose colors to be used in the design.

Requirements
Must have
• The size of the mailer should be about 6 by 8 inches.
• Two sides.
• Side 1: With our Logo and key messages we want to communicate.
• Side 2: A space to be used by the USA mail services in lower right, my photo and an introduction by me to our company and why they should buy from my company.
Nice to have
• Images that represent what we do, how we help, and our target market.
Should not have
• Poor taste in images that upset people

```html
<!DOCTYPE html>
<html lang="en">
<head>
<meta charset="utf-8">
<title>Quik Path Prospects – Postcard Mailer</title>
<link href="https://fonts.googleapis.com/css2?family=Lato:ital,wght@0,300;0,400;0,700;0,900;1,400;1,700&family=Montserrat:wght@500;600;700;800&display=swap" rel="stylesheet">
<style>
:root{
  --stage:#2a2a2c;
  --navy-deep:#15233a;
  --brand-blue:#1565b0;
  --royal:#0f5ea8;
  --cyan:#45c3ee;
  --ink:#2b2b2b;
  --charcoal:#3a3a3c;
  --grey:#595a5c;
  --white:#ffffff;
}
*{box-sizing:border-box;margin:0;padding:0}
html,body{width:902px;height:1200px;overflow:hidden}
body{background:var(--stage);font-family:"Lato",Arial,sans-serif;position:relative}

.card{position:absolute;left:80px;width:669px;height:500px;background:var(--white);overflow:hidden;box-shadow:0 4px 14px rgba(0,0,0,.45)}
.card--front{top:80px}
.card--back{top:618px;left:154px}

/* ---------- FRONT ---------- */
.word-cloud{position:absolute;left:0;top:0;width:340px;height:436px;overflow:hidden;
  background:radial-gradient(ellipse at 30% 40%,#3d5573 0%,#243752 45%,var(--navy-deep) 100%);color:var(--white)}
.word-cloud span{position:absolute;white-space:nowrap;line-height:1}
.w-light{font-weight:300}
.w-bold{font-weight:700}
.w-faint{opacity:.5}
.cloud-name{font-family:"Montserrat",sans-serif;font-weight:700;color:var(--cyan);font-size:21px;letter-spacing:0}

.brand-block{position:absolute;display:flex;align-items:center;gap:8px}
.brand-square{width:16px;height:16px;background:var(--brand-blue);flex:none}
.brand-name{font-family:"Montserrat",sans-serif;font-weight:700;color:var(--brand-blue);line-height:1.05}
.card--front .brand-block{left:380px;top:30px;width:260px}
.card--front .brand-name{font-size:26px}

.feature-img{position:absolute;width:124px;height:100px;border:1px solid #8a8a8a}
.img-stairs{background:linear-gradient(180deg,#ffffff 0%,#dfe6ee 60%,#6f8fb3 100%)}
.img-tech{background:linear-gradient(160deg,#b9c6d6 0%,#4d6f96 55%,#1f3552 100%)}
.img-hands{background:linear-gradient(150deg,#8fb1d6 0%,#5f8cc0 50%,#d9b7a3 100%)}
.img-gavel{background:radial-gradient(circle at 50% 60%,#e8c04a 0%,#f4f4f4 55%,#ffffff 100%)}

.feature{position:absolute;width:140px}
.feature h3{font-family:"Montserrat",sans-serif;font-weight:700;font-size:8px;color:var(--brand-blue);letter-spacing:.2px;margin-bottom:4px}
.feature li{list-style:none;position:relative;padding-left:10px;font-style:italic;font-size:7px;color:var(--ink);margin-bottom:5px;line-height:1.25}
.feature li::before{content:"";position:absolute;left:0;top:2px;width:4px;height:4px;border-radius:50%;background:var(--brand-blue)}

.contact-band{position:absolute;left:0;top:436px;width:669px;height:64px}
.contact-band svg.band-bg{position:absolute;left:0;top:0}
.band-name{position:absolute;left:17px;top:10px;color:var(--white)}
.band-name strong{display:block;font-size:15px;font-weight:700}
.band-name small{display:block;font-size:8.5px}
.band-phone{position:absolute;left:140px;top:8px;display:flex;align-items:center;gap:8px;color:var(--white);font-family:"Montserrat",sans-serif;font-weight:700;font-size:24px}
.band-email{position:absolute;left:420px;top:9px;display:flex;align-items:center;gap:9px;color:var(--white);font-size:15px}

/* ---------- BACK ---------- */
.intro-top{position:absolute;left:0;top:0;width:378px;height:163px;background:var(--royal)}
.portrait{position:absolute;left:33px;top:29px;width:110px;height:133px;border:3px solid var(--white);
  background:linear-gradient(180deg,#d8dde3 0%,#b8bec6 55%,#2e3440 100%)}
.name-tag{position:absolute;left:143px;top:66px;width:235px;height:39px;padding:5px 0 0 12px;
  background:linear-gradient(90deg,#b9b9b9 0%,#e6e6e6 40%,#ffffff 100%);font-weight:700;font-size:11px;color:var(--charcoal);line-height:1.35}
.intro-head{position:absolute;left:0;top:163px;width:378px;height:55px;background:var(--grey);padding:9px 0 0 28px;
  font-family:"Montserrat",sans-serif;font-weight:700;font-size:15px;color:var(--white);line-height:1.35;letter-spacing:.2px}
.intro-list{position:absolute;left:25px;top:238px;width:345px;list-style:none}
.intro-list li{position:relative;padding-left:24px;font-size:10.5px;color:var(--ink);line-height:1.32;margin-bottom:4px}
.intro-list li svg{position:absolute;left:0;top:2px}
.mission{position:absolute;left:0;top:392px;width:378px;height:84px;background:var(--royal);padding:9px 10px 0 36px;
  font-style:italic;font-weight:700;font-size:16.5px;color:var(--white);line-height:1.4;white-space:nowrap}
.foot-strip{position:absolute;left:0;bottom:0;width:669px;height:24px;background:var(--grey)}
.divider{position:absolute;left:378px;top:0;width:1px;height:476px;background:#cfd3d8}

.card--back .brand-block{left:412px;top:36px;width:220px}
.card--back .brand-name{font-size:22px}
.tagline{position:absolute;left:378px;top:110px;width:291px;text-align:center;font-style:italic;font-weight:700;font-size:8.5px;color:var(--charcoal);line-height:1.45}
.test-head{position:absolute;left:396px;top:148px;font-family:"Montserrat",sans-serif;font-weight:700;font-size:15px;color:var(--brand-blue);letter-spacing:.4px}
.test-list{position:absolute;left:396px;top:174px;list-style:none}
.test-list li{position:relative;padding-left:24px;font-style:italic;font-weight:700;font-size:12.5px;color:var(--ink);margin-bottom:6px;white-space:nowrap}
.test-list li::before{content:"";position:absolute;left:2px;top:4px;width:8px;height:8px;border-radius:50%;background:var(--brand-blue)}

.mail-area{position:absolute;left:378px;top:256px;width:275px;height:220px;border-top:1px solid #c4c8cd;border-right:1px solid #c4c8cd}
.return-address{position:absolute;left:14px;top:14px;font-size:7.5px;color:var(--charcoal);line-height:1.4}
.stamp-box{position:absolute;left:190px;top:12px;width:68px;height:60px;border:1px solid #b5b9be}
.address-line{position:absolute;left:58px;width:200px;height:1px;background:#8d9196}
</style>
</head>
<body>

<section class="card card--front">
  <div class="word-cloud" role="img" aria-label="Dark blue photo of reaching hands behind a cloud of key words">
    <span class="w-bold" style="left:27px;top:42px;font-size:11px">Tailored Campaigns</span>
    <span class="w-bold" style="left:133px;top:40px;font-size:14px">Passion</span>
    <span style="left:192px;top:43px;font-size:9px">100 years of cumulative experience</span>
    <span class="w-faint" style="left:28px;top:65px;font-size:8px">Technology SaVVY</span>
    <span class="w-light" style="left:108px;top:61px;font-size:15px">Proprietary Software and Methods</span>
    <span style="left:28px;top:87px;font-size:8.5px">LOW COST ACQUISITION</span>
    <span class="w-bold" style="left:135px;top:84px;font-size:14px">Best Leads, Best Price</span>
    <span style="left:283px;top:86px;font-size:10px">Exclusivity</span>
    <span class="w-light" style="left:27px;top:111px;font-size:13px">Best Conversion Rates</span>
    <span class="w-light" style="left:176px;top:110px;font-size:15px">SSD Domain Expertise</span>
    <span style="left:29px;top:139px;font-size:18px">Deep business and process acumen</span>
    <span style="left:27px;top:174px;font-size:12px">Quality Standards</span>
    <span class="w-light" style="left:172px;top:172px;font-size:17px">Systems Integration</span>
    <span class="cloud-name" style="left:36px;top:209px">QUIK PATH PROSPECTS</span>
    <span style="left:27px;top:245px;font-size:17px">Highest ROI</span>
    <span style="left:258px;top:244px;font-size:12px">Referrals</span>
    <span class="w-bold" style="left:25px;top:269px;font-size:21px">Reliable, Dependable, Helpful</span>
    <span style="left:28px;top:301px;font-size:10.5px">Tested leads generation practices</span>
    <span style="left:195px;top:300px;font-size:12px">Great data mining &amp; filters</span>
    <span style="left:21px;top:321px;font-size:14px">Trusted Partner</span>
    <span class="w-faint" style="left:151px;top:321px;font-size:14px">Experienced at outsourcing</span>
    <span class="w-faint" style="left:21px;top:346px;font-size:10px">Technology R&amp;D Investment</span>
    <span style="left:215px;top:344px;font-size:15px">Exclusivity</span>
    <span style="left:48px;top:366px;font-size:13px">Easy to use</span>
    <span class="w-faint" style="left:163px;top:367px;font-size:10px">Benchmarking &amp; Consulting</span>
    <span style="left:21px;top:389px;font-size:12px">High Volume Generation</span>
    <span style="left:167px;top:388px;font-size:13px">Age Demographics (35 to 64)</span>
  </div>

  <div class="brand-block">
    <span class="brand-square"></span>
    <span class="brand-name">QUIK PATH PROSPECTS</span>
  </div>

  <div class="feature-img img-stairs" style="left:376px;top:117px" role="img" aria-label="Business people climbing rising bar chart steps"></div>
  <div class="feature-img img-tech" style="left:514px;top:117px" role="img" aria-label="Businessman holding a tablet with network icons"></div>
  <div class="feature-img img-hands" style="left:376px;top:282px" role="img" aria-label="Caring hand holding an elderly hand"></div>
  <div class="feature-img img-gavel" style="left:514px;top:282px" role="img" aria-label="Figure in a wheelchair beside a golden gavel"></div>

  <div class="feature" style="left:376px;top:229px">
    <h3>BEST LEADS, BEST PRICE</h3>
    <ul>
      <li>Our high conversation rates lowers your client acquisition cost</li>
      <li>Referrals available</li>
    </ul>
  </div>
  <div class="feature" style="left:514px;top:229px">
    <h3>HIGH VOLUME, QUALITY LEADS</h3>
    <ul>
      <li>50 years of SSD domain knowledge</li>
      <li>Tested technology capabilities</li>
    </ul>
  </div>
  <div class="feature" style="left:376px;top:395px">
    <h3>TRUSTED PARTNER</h3>
    <ul>
      <li>Reliability, Dependable, Helpful</li>
      <li>Deep business &amp; process acumen</li>
    </ul>
  </div>
  <div class="feature" style="left:514px;top:395px">
    <h3>EASY TO USE</h3>
    <ul>
      <li>Integrate seamlessly into your IT systems</li>
      <li>Tailored campaigns</li>
    </ul>
  </div>

  <div class="contact-band">
    <svg class="band-bg" width="669" height="64" viewBox="0 0 669 64" aria-hidden="true">
      <defs>
        <linearGradient id="bandBlue" x1="0" x2="1" y1="0" y2="0">
          <stop offset="0" stop-color="#1f4f9c"/>
          <stop offset="1" stop-color="#3fa6e6"/>
        </linearGradient>
      </defs>
      <rect width="669" height="64" fill="url(#bandBlue)"/>
      <polygon points="376,0 669,0 669,40 418,40" fill="#2f3033"/>
      <polygon points="418,40 669,40 669,64 440,64" fill="#45c3ee"/>
      <polygon points="372,0 376,0 418,40 414,40" fill="#ffffff" opacity=".7"/>
    </svg>
    <div class="band-name">
      <strong>Martin Kessler,</strong>
      <small>President Quik Path Prospects</small>
    </div>
    <div class="band-phone">
      <svg width="22" height="22" viewBox="0 0 22 22" aria-hidden="true">
        <circle cx="11" cy="11" r="10" fill="none" stroke="#fff" stroke-width="1.6"/>
        <path d="M7.5 6.2l1.8-.4 1 2.4-1.2.9c.6 1.4 1.6 2.4 3 3l.9-1.2 2.4 1-.4 1.8c-4 .2-7.7-3.5-7.5-7.5z" fill="#fff"/>
      </svg>
      <span>555-014-2277</span>
    </div>
    <div class="band-email">
      <svg width="16" height="12" viewBox="0 0 16 12" aria-hidden="true">
        <rect x="0.5" y="0.5" width="15" height="11" fill="#fff"/>
        <path d="M1 1l7 6 7-6" fill="none" stroke="#2f3033" stroke-width="1.3"/>
      </svg>
      <span>martin@quikpathprospects.com</span>
    </div>
  </div>
</section>

<section class="card card--back">
  <div class="intro-top">
    <div class="portrait" role="img" aria-label="Portrait photo of the company president"></div>
    <div class="name-tag">Martin Kessler<br>President, Quik Path Prospects</div>
  </div>
  <div class="intro-head">I WANT TO PERSONALLY INTRODUCE<br>OUR COMPANY TO YOU!</div>

  <ul class="intro-list">
    <li><svg width="11" height="11" viewBox="0 0 11 11" aria-hidden="true"><circle cx="5.5" cy="5.5" r="4.8" fill="none" stroke="#1565b0" stroke-width="1"/><path d="M4.5 3.3l2.2 2.2-2.2 2.2" fill="none" stroke="#1565b0" stroke-width="1"/></svg>My team as &gt; 50 years of cumulative SSD experience.</li>
    <li><svg width="11" height="11" viewBox="0 0 11 11" aria-hidden="true"><circle cx="5.5" cy="5.5" r="4.8" fill="none" stroke="#1565b0" stroke-width="1"/><path d="M4.5 3.3l2.2 2.2-2.2 2.2" fill="none" stroke="#1565b0" stroke-width="1"/></svg>We have proven technology that delivers the best leads.</li>
    <li><svg width="11" height="11" viewBox="0 0 11 11" aria-hidden="true"><circle cx="5.5" cy="5.5" r="4.8" fill="none" stroke="#1565b0" stroke-width="1"/><path d="M4.5 3.3l2.2 2.2-2.2 2.2" fill="none" stroke="#1565b0" stroke-width="1"/></svg>The timing is right for a new competitor in this industry.</li>
    <li><svg width="11" height="11" viewBox="0 0 11 11" aria-hidden="true"><circle cx="5.5" cy="5.5" r="4.8" fill="none" stroke="#1565b0" stroke-width="1"/><path d="M4.5 3.3l2.2 2.2-2.2 2.2" fill="none" stroke="#1565b0" stroke-width="1"/></svg>I had to come out of retirement after 30 years with Norvale Corp, the opportunity is just that great … I love building businesses and partnering with great customers!</li>
    <li><svg width="11" height="11" viewBox="0 0 11 11" aria-hidden="true"><circle cx="5.5" cy="5.5" r="4.8" fill="none" stroke="#1565b0" stroke-width="1"/><path d="M4.5 3.3l2.2 2.2-2.2 2.2" fill="none" stroke="#1565b0" stroke-width="1"/></svg>Our business, industry, &amp; technical acumen is unrivaled … and we can do it at a cost than no others can.</li>
  </ul>

  <div class="mission">Let’s work together to bring Social<br>Security Disability benefits to those<br>in need and deserving!</div>

  <div class="divider"></div>

  <div class="brand-block">
    <span class="brand-square"></span>
    <span class="brand-name">QUIK PATH PROSPECTS</span>
  </div>
  <p class="tagline">Best Leads … Best Price with High Volume &amp; Quality capacity …<br>Leads from a Trusted Partner that is easy to use</p>

  <h2 class="test-head">TEST OUR LEADS</h2>
  <ul class="test-list">
    <li>Start at 250 or 500 Leads.</li>
    <li>Grow to 1,000 … 3,000 or even 10,000!</li>
    <li>We give the right support to your growth.</li>
  </ul>

  <div class="mail-area">
    <p class="return-address">Martin Kessler, President Quik Path Prospects<br>1200 Sample Avenue, Suite 300<br>Springfield OH 45000<br>555-014-2277<br>martin@quikpathprospects.com</p>
    <div class="stamp-box"></div>
    <div class="address-line" style="top:116px"></div>
    <div class="address-line" style="top:147px"></div>
    <div class="address-line" style="top:179px"></div>
  </div>

  <div class="foot-strip"></div>
</section>

</body>
</html>
```